Brennick Drilling Inc. Business card design

Business card design for "Brennick Drilling Inc. - Directional Drilling Services"

Address is:

Brennick Drilling Inc.
512 - 73 Tarvel Crescent SW
Calgary, Alberta, Canada
T2K 4P8

Please incorporate the logo design into the card, thank you.

Target Market(s)

Oil & Gas and Drilling

Industry/Entity Type

Business

```html
<!DOCTYPE html>
<html lang="en">
<head>
<meta charset="utf-8">
<title>Brennick Drilling Inc. Business Card</title>
<link rel="stylesheet" href="https://fonts.googleapis.com/css2?family=Ubuntu:wght@400;500;700&display=swap">
<style>
  :root {
    --bg: #e4e5e7;
    --black: #1f1d1e;
    --ink: #231f20;
    --red: #d9272b;
    --orange: #f39220;
    --grey: #bcbdc0;
    --white: #ffffff;
    --muted: #8a8b8e;
  }
  * { box-sizing: border-box; margin: 0; padding: 0; }
  html, body { width: 1200px; height: 1000px; overflow: hidden; }
  body {
    background: var(--bg);
    font-family: "Ubuntu", sans-serif;
    position: relative;
  }
  .card {
    position: absolute;
    left: 270px;
    width: 660px;
    height: 380px;
    border-radius: 22px;
    overflow: hidden;
    box-shadow: 0 10px 26px rgba(0,0,0,0.18);
  }
  .card-front { top: 70px; }
  .card-back { top: 540px; background: var(--white); }
  .card-art { position: absolute; inset: 0; width: 100%; height: 100%; display: block; }

  /* Front */
  .brand-mark {
    position: absolute;
    left: 258px;
    top: 70px;
    width: 96px;
    height: 96px;
    border-radius: 50%;
    border: 4px solid var(--white);
  }
  .brand-name {
    position: absolute;
    left: 150px;
    top: 196px;
    font-weight: 700;
    font-size: 33px;
    letter-spacing: 1px;
    color: var(--white);
    text-transform: uppercase;
  }
  .brand-tagline {
    position: absolute;
    left: 152px;
    top: 240px;
    font-weight: 500;
    font-size: 15px;
    letter-spacing: 3.4px;
    color: #e6e7e8;
    text-transform: uppercase;
  }
  .brand-web {
    position: absolute;
    left: 322px;
    top: 296px;
    font-size: 15px;
    letter-spacing: 1px;
    color: var(--muted);
  }

  /* Back */
  .person-name {
    position: absolute;
    left: 48px;
    top: 76px;
    font-weight: 700;
    font-size: 23px;
    color: var(--red);
  }
  .person-role {
    position: absolute;
    left: 48px;
    top: 108px;
    font-size: 15px;
    color: var(--white);
  }
  .contact-lines {
    position: absolute;
    left: 318px;
    top: 76px;
    font-size: 15px;
    line-height: 22px;
    color: var(--white);
  }
  .company-name {
    position: absolute;
    left: 56px;
    top: 206px;
    font-weight: 700;
    font-size: 19px;
    color: var(--red);
    text-transform: uppercase;
  }
  .company-address {
    position: absolute;
    left: 56px;
    top: 240px;
    font-size: 17px;
    line-height: 22px;
    color: var(--ink);
  }
</style>
</head>
<body>

  <section class="card card-front" aria-label="Business card front">
    <svg class="card-art" viewBox="0 0 660 380" aria-hidden="true">
      <defs>
        <linearGradient id="cornerSplit" x1="0" y1="1" x2="1" y2="0">
          <stop offset="0.5" stop-color="#f39220"/>
          <stop offset="0.5" stop-color="#bcbdc0"/>
        </linearGradient>
      </defs>
      <rect width="660" height="380" fill="url(#cornerSplit)"/>
      <circle cx="400" cy="140" r="310" fill="#ffffff"/>
      <circle cx="330" cy="200" r="310" fill="#d9272b"/>
      <circle cx="360" cy="170" r="285" fill="#1f1d1e"/>
    </svg>
    <div class="brand-mark" aria-hidden="true"></div>
    <div class="brand-name">Brennick Drilling Inc.</div>
    <div class="brand-tagline">Directional Drilling Services</div>
    <div class="brand-web">www.BrennickDrilling.com</div>
  </section>

  <section class="card card-back" aria-label="Business card back">
    <svg class="card-art" viewBox="0 0 660 380" aria-hidden="true">
      <rect width="660" height="380" fill="#ffffff"/>
      <g fill="none">
        <circle class="arc-grey" cx="620" cy="300" r="270" stroke="#bcbdc0" stroke-width="40"/>
        <path class="arc-orange" d="M 545 -10 A 230 230 0 0 1 650 260" stroke="#f39220" stroke-width="30"/>
        <path class="arc-red" d="M 490 -10 A 210 210 0 0 1 610 280" stroke="#d9272b" stroke-width="26"/>
        <circle class="arc-black" cx="600" cy="190" r="210" stroke="#231f20" stroke-width="26"/>
      </g>
      <rect class="contact-band" x="0" y="58" width="660" height="92" fill="#231f20"/>
    </svg>
    <div class="person-name">Alex Reddan</div>
    <div class="person-role">Accountant</div>
    <div class="contact-lines">
      <div>+1 403 555 0188</div>
      <div>alex@BrennickDrilling.com</div>
    </div>
    <div class="company-name">Brennick Drilling Inc.</div>
    <div class="company-address">
      512 - 73 Tarvel Crescent SW<br>
      Calgary, Alberta, Canada<br>
      T2K 4P8
    </div>
  </section>

</body>
</html>
```